Upbeat Accouting Package Flyer

I am looking for a 1 page (front, or front and back) flyer that will become our marketing for our accounting services. We are looking for something a little different and we are catering to the small retail shop owners. We have 3 accounting packages we would like to display and then some add-ons. I have included our logo that must be included in the design. I have uploaded the accounting package information as well.
Target Market(s)
Small Retail Shop Owners
Industry/Entity Type
Accounting
Colors
Designer to choose colors to be used in the design.
Requirements
Must have
- A casual feel. We are not your typical accountants who are very professional and "stuffy". I want it to feel like we are all family.
Nice to have
- I would like to incorporate some sort of retail theme.
- We have a couple of taglines we like to use and it would be great if they could be included. They are "We know you CAN do the accounting, but do you WANT to?" and "We allow you to get back to what's important."
Should not have
- Typical stock accounting photos of people shaking hands, large office buildings, etc.

```html
<!DOCTYPE html>
<html lang="en">
<head>
<meta charset="utf-8">
<title>Accounting Packages Flyer</title>
<link href="https://fonts.googleapis.com/css2?family=Arimo:wght@400;700&family=Kalam:wght@700&display=swap" rel="stylesheet">
<style>
  :root {
    --ink: #1c1c1c;
    --accent-red: #e0262b;
    --teal: #1aa79c;
    --charcoal: #3f3f41;
    --develop-dark: #1b5a8e;
    --develop-light: #4a90c9;
    --grow-dark: #4b9250;
    --grow-light: #62c46e;
    --relax-dark: #f7931e;
    --relax-light: #fbbf69;
    --options-grey: #a7a9ac;
    --brand-teal: #1ab0c8;
    --frame: #555;
  }
  * { box-sizing: border-box; margin: 0; padding: 0; }
  html, body { width: 1200px; height: 1000px; overflow: hidden; background: #fff; }
  body { position: relative; font-family: "Arimo", Arial, sans-serif; color: var(--ink); }

  .flyer {
    position: absolute; left: 302px; top: 62px; width: 596px; height: 842px;
    border: 1px solid var(--frame); background: #fff; overflow: hidden;
  }
  .hero-tagline {
    position: absolute; left: 22px; top: 22px; width: 268px; z-index: 2;
    font-family: "Kalam", cursive; font-weight: 700; font-size: 25px; line-height: 43px;
    letter-spacing: -0.4px; white-space: nowrap; color: var(--ink);
  }
  .hero-tagline em { font-style: normal; color: var(--accent-red); }
  .hero-photo {
    position: absolute; left: 293px; top: 0; width: 303px; height: 202px;
    background: linear-gradient(135deg, #8a6f55 0%, #c9a98a 40%, #6b5a4a 75%, #3a3431 100%);
  }
  .section-label {
    position: absolute; left: 0; top: 173px; width: 293px; height: 29px;
    background: linear-gradient(90deg, var(--teal) 0%, var(--teal) 75%, #fff 100%);
    color: #fff; font-size: 21px; line-height: 29px; padding-left: 30px;
  }

  .package { position: absolute; left: 0; width: 596px; }
  .package-head { position: relative; height: 60px; }
  .package-head svg { position: absolute; left: 0; top: 0; }
  .package-name {
    position: absolute; left: 0; top: 0; width: 290px; height: 60px;
    color: #fff; font-size: 19px; line-height: 60px; text-align: center;
  }
  .package-price {
    position: absolute; left: 322px; top: 12px; color: #fff; font-size: 16px; line-height: 20px;
  }
  .package-price b { font-weight: 700; }
  .package-body { display: flex; padding: 11px 10px 0 16px; font-size: 12px; line-height: 14.5px; color: #222; }
  .package-body ul { list-style: none; }
  .package-body li { position: relative; padding-left: 10px; }
  .package-body li::before { content: "•"; position: absolute; left: 0; }
  .package-body ul:first-child { width: 286px; }
  .package-body ul:last-child { width: 278px; }

  .develop { top: 211px; }
  .develop .package-body { background: var(--develop-light); height: 75px; }
  .grow { top: 356px; }
  .grow .package-body { background: var(--grow-light); height: 125px; color: #fff; }
  .relax { top: 551px; }
  .relax .package-body { background: var(--relax-light); height: 124px; color: #fff; }

  .add-ons {
    position: absolute; left: 14px; top: 749px; width: 306px; height: 81px;
    background: var(--options-grey); border-radius: 10px; color: #fff;
    padding: 9px 16px; font-size: 9.5px; line-height: 12px;
  }
  .add-ons h3 { font-size: 9.5px; font-weight: 700; }
  .brand {
    position: absolute; left: 350px; top: 764px; display: flex; align-items: center; gap: 9px;
  }
  .brand-mark { width: 16px; height: 16px; background: var(--brand-teal); border-radius: 50%; }
  .brand-name { font-size: 18px; font-weight: 700; color: var(--charcoal); line-height: 1.15; }
</style>
</head>
<body>
  <div class="flyer">
    <h1 class="hero-tagline">We know you <em>CAN</em> do<br>the accounting, but<br>do you <em>WANT</em> to?</h1>
    <div class="hero-photo" role="img" aria-label="Photo of three women laughing together around a café table"></div>
    <div class="section-label">Accounting Packages</div>

    <section class="package develop">
      <div class="package-head">
        <svg width="596" height="60" aria-hidden="true">
          <rect x="0" y="0" width="596" height="60" fill="var(--charcoal)"/>
          <polygon points="0,0 278,0 308,30 278,60 0,60" fill="var(--develop-dark)"/>
        </svg>
        <div class="package-name">Develop</div>
        <div class="package-price"><b>$300/mo</b> when paid annually<br><b>$325/mo</b> billed monthly</div>
      </div>
      <div class="package-body">
        <ul>
          <li>LedgerLine Online subscription</li>
          <li>Free accounting setup</li>
          <li>Weekly transaction processing</li>
        </ul>
        <ul>
          <li>Monthly account reconciliation (up to 2 accounts)</li>
          <li>Monthly financial statements by the 15th of the month</li>
        </ul>
      </div>
    </section>

    <section class="package grow">
      <div class="package-head">
        <svg width="596" height="60" aria-hidden="true">
          <rect x="0" y="0" width="596" height="60" fill="var(--charcoal)"/>
          <polygon points="0,0 278,0 308,30 278,60 0,60" fill="var(--grow-dark)"/>
        </svg>
        <div class="package-name">Grow</div>
        <div class="package-price"><b>$550/mo</b> billed annually;<br><b>$575/mo</b> billed monthly</div>
      </div>
      <div class="package-body">
        <ul>
          <li>LedgerLine Online subscription</li>
          <li>Free accounting setup</li>
          <li>Weekly transaction processing</li>
          <li>Monthly account reconciliation (up to 4 accounts)</li>
          <li>Monthly financial statements by the 10th of the month</li>
        </ul>
        <ul>
          <li>Client portal access for document sharing</li>
          <li>1 Custom Report</li>
          <li>Accounts Payable</li>
          <li>Monthly Scorecard (customized metric tracking for your business)</li>
        </ul>
      </div>
    </section>

    <section class="package relax">
      <div class="package-head">
        <svg width="596" height="60" aria-hidden="true">
          <rect x="0" y="0" width="596" height="60" fill="var(--charcoal)"/>
          <polygon points="0,0 278,0 308,30 278,60 0,60" fill="var(--relax-dark)"/>
        </svg>
        <div class="package-name">Relax (We’ve Got This)</div>
        <div class="package-price"><b>$850/mo</b> billed annually;<br><b>$875/mo</b> billed monthly</div>
      </div>
      <div class="package-body">
        <ul>
          <li>LedgerLine Online subscription</li>
          <li>Free accounting setup</li>
          <li>Weekly transaction processing</li>
          <li>Monthly account reconciliation (up to 5-10 accounts)</li>
          <li>Monthly financial statements by the 5th of the month</li>
        </ul>
        <ul>
          <li>Client portal access for document sharing</li>
          <li>2 Custom Reports</li>
          <li>Accounts Payable</li>
          <li>Invoicing and accounts receivable</li>
          <li>Weekly Scorecard (customized metric tracking for your business)</li>
        </ul>
      </div>
    </section>

    <aside class="add-ons">
      <h3>Additional Options</h3>
      <p>Payroll – 1-10 employees $85/mo; 11-30 employees $175/mo</p>
      <p>Sales tax - $30/mo per state</p>
      <p>Corporate taxes $50/mo</p>
      <p>Owner taxes - $25/mo</p>
    </aside>

    <div class="brand">
      <span class="brand-mark"></span>
      <span class="brand-name">Brightleaf Tax<br>and Accounting Inc.</span>
    </div>
  </div>
</body>
</html>
```